Stationary/business card/envelope design for Ravenhill Dentalcare

We are located in the foothills of the sierra nevada mountains. We are looking for a beautiful classy modern stationary. We need evelopes and business card design all to flow seamlessly. Envelope design.

Additional office address 4816 Orchard Crest Rd., Suite B, Auburn, CA 95604 Phone: pending Fax: pending.

3 different Drs on each business card:
Marla J. Whitcombe, DDS
Tessa R. Whitcombe, DDS
Rosalind P. Haverty, DDS

Target Market(s)

Dental patients

Industry/Entity Type

Dental

Contact Information for Business Card

Two sided. See example.

Font styles to use
Sans Serif

Requirements
Must have
• One sided business cards. Need envelope design.
Colors should match existing logo.

Marla J. Whitcombe, DDS
Tessa R. Whitcombe, DDS
Rosalind P. Haverty, DDS

```html
<!DOCTYPE html>
<html lang="en">
<head>
<meta charset="utf-8">
<title>Ravenhill Dentalcare Stationery</title>
<link href="https://fonts.googleapis.com/css2?family=Roboto:wght@400;700&display=swap" rel="stylesheet">
<style>
  :root {
    --backdrop: #e2e2e2;
    --paper: #ffffff;
    --brand-green: #1f6b33;
    --brand-blue: #3fb1dc;
    --ink: #222222;
    --fold-line: #c9c9c9;
  }
  html, body {
    margin: 0;
    padding: 0;
    width: 1196px;
    height: 1200px;
    overflow: hidden;
    background: var(--backdrop);
    font-family: "Roboto", sans-serif;
    color: var(--ink);
  }
  .canvas { position: relative; width: 1196px; height: 1200px; }
  .sheet { position: absolute; background: var(--paper); box-sizing: border-box; }

  .business-card { left: 455px; top: 216px; width: 334px; height: 192px; }
  .doctor-name {
    position: absolute; left: 25px; top: 48px; margin: 0;
    font-size: 12.5px; font-weight: 700; color: var(--brand-green); letter-spacing: 0.1px;
  }
  .doctor-title { position: absolute; left: 25px; top: 65px; margin: 0; font-size: 9px; }
  .contact-list {
    position: absolute; left: 25px; top: 100px; margin: 0; padding: 0; list-style: none;
    font-size: 8.6px; line-height: 11.5px;
  }
  .contact-list li { display: flex; align-items: flex-start; }
  .contact-list li.address { margin-bottom: 6px; }
  .contact-list svg { width: 8px; height: 8px; margin: 2px 4px 0 0; flex: none; fill: var(--brand-green); }

  .brand-mark { position: absolute; display: flex; flex-direction: column; align-items: center; }
  .brand-mark .mark-circle { border-radius: 50%; background: var(--brand-blue); }
  .brand-mark .brand-name {
    color: var(--brand-green); font-weight: 700; white-space: nowrap; text-align: center; line-height: 1.15;
  }
  .business-card .brand-mark { left: 208px; top: 22px; width: 96px; }
  .business-card .mark-circle { width: 58px; height: 58px; margin-bottom: 6px; }
  .business-card .brand-name { font-size: 11px; }

  .envelope-front { left: 353px; top: 451px; width: 537px; height: 233px; }
  .envelope-front .brand-mark { left: 22px; top: 22px; width: 80px; }
  .envelope-front .mark-circle { width: 48px; height: 48px; margin-bottom: 5px; }
  .envelope-front .brand-name { font-size: 9px; }
  .return-address { position: absolute; left: 28px; top: 97px; margin: 0; font-size: 9px; line-height: 12.5px; font-style: normal; }
  .envelope-web { position: absolute; left: 28px; top: 199px; margin: 0; font-size: 9px; }

  .envelope-back { left: 353px; top: 725px; width: 537px; height: 233px; }
  .envelope-back .flap { position: absolute; left: 0; top: 0; }
  .envelope-back .brand-mark { left: 228px; top: 20px; width: 80px; }
  .envelope-back .mark-circle { width: 34px; height: 34px; margin-bottom: 4px; }
  .envelope-back .brand-name { font-size: 7px; }
</style>
</head>
<body>
<main class="canvas">

  <section class="sheet business-card" aria-label="Business card">
    <h1 class="doctor-name">MARLA J. WHITCOMBE, DDS</h1>
    <p class="doctor-title">Family &amp; Cosmetic Dentistry</p>
    <ul class="contact-list">
      <li class="address">
        <svg viewBox="0 0 10 10"><path d="M5 0a3.5 3.5 0 0 0-3.5 3.5C1.5 6 5 10 5 10s3.5-4 3.5-6.5A3.5 3.5 0 0 0 5 0zm0 5a1.4 1.4 0 1 1 0-2.8A1.4 1.4 0 0 1 5 5z"/></svg>
        <span>4816 Orchard Crest Rd.<br>Suite B, Auburn, CA 95604</span>
      </li>
      <li>
        <svg viewBox="0 0 10 10"><path d="M2 1l2 2-1 1c.6 1.3 1.7 2.4 3 3l1-1 2 2-1.5 1.5C4 9 1 6 .5 2.5z"/></svg>
        <span>(123) 123 1234</span>
      </li>
      <li>
        <svg viewBox="0 0 10 10"><rect x="2" y="1" width="6" height="3"/><rect x="0.5" y="4" width="9" height="4" rx="1"/></svg>
        <span>(123) 123 1234</span>
      </li>
      <li>
        <svg viewBox="0 0 10 10"><path d="M0 2h10v6H0zm1 1v.3l4 2.6 4-2.6V3z"/></svg>
        <span>info@RavenhillDentalcare.com</span>
      </li>
      <li>
        <svg viewBox="0 0 10 10"><circle cx="5" cy="5" r="4.5"/></svg>
        <span>www.RavenhillDentalcare.com</span>
      </li>
    </ul>
    <div class="brand-mark">
      <span class="mark-circle"></span>
      <span class="brand-name">Ravenhill Dentalcare</span>
    </div>
  </section>

  <section class="sheet envelope-front" aria-label="Envelope front">
    <div class="brand-mark">
      <span class="mark-circle"></span>
      <span class="brand-name">Ravenhill Dentalcare</span>
    </div>
    <address class="return-address">4816 Orchard Crest Rd.<br>Suite B, Auburn, CA 95604</address>
    <p class="envelope-web">www.RavenhillDentalcare.com</p>
  </section>

  <section class="sheet envelope-back" aria-label="Envelope back">
    <svg class="flap" width="537" height="96" viewBox="0 0 537 96">
      <path d="M0.5 0 L12 72 Q18 92 40 92 L497 92 Q519 92 525 72 L536.5 0" fill="none" stroke="var(--fold-line)" stroke-width="1"/>
    </svg>
    <div class="brand-mark">
      <span class="mark-circle"></span>
      <span class="brand-name">Ravenhill Dentalcare</span>
    </div>
  </section>

</main>
</body>
</html>
```